**URGENT // ENVIRONMENTAL // QUICK TURN AROUND**

We are looking for an A-Grade designer to work with longterm, starting with the successful design for our website & logo; Kestrel Hub.

Kestrel Hub is a business that focusses on grouping environmentally conscious people together and helping them get "bulk buy" discounts by purchasing large volumes together; solar, energy efficency, wind turbines, and the like.

The Logo and website must have a green feel, as we are here to protect the environment, whilst also helping our customers save money.

The website must also have a blog feature, allowing us to post and keep people up to date with the latest in the industry.

Target Market(s)

FAMILIES WITHIN REGIONAL AUSTRALIA WANTING TO EITHER SAVE MONEY ON ELECTRICITY BILLS, OR REDUCE CARBON EMISSIONS.

Industry/Entity Type

Solar Energy

Logo Text

KESTREL HUB

Number of Pages Required

5+ page

Font styles to use
Serif
Sans Serif

Colors

Designer to choose colors to be used in the design.

Requirements
Must have
• 1.HOME PAGE
• 2.OUR SERVICES PAGE
• - RENEWABLE ENERGY
• - LIGHTING SYSTEMS
• - ENERGY ASSESSMENT
• - R.H.L.P SCHEME
• - ENERGY COMPARISON
• 4. BOOK AN APPOINTMENT
• 5. IN THE NEWS
• 6. SUBSCRIBE TO NEWSLETTER
• 7. CONTACT US
• MUST LOOK VERY PROFESSIONAL, WITH LOTS OF INFORMATION, IT CANNOT BE BARE AND SIMPLE.
• Can use www.tarnfieldgoodsandwares.com.au which is our other brand for copy and ideas - HOWEVER, THIS IS THE REASON WE ARE RE-BRANDING, AS THIS BRAND HAS COME UNDER FAR TOO MUCH CRITICISM FOR LACK OF INFORMATION AND LOOKING TO SIMPLE.
Nice to have
• BLOG FEATURE
Should not have
• ANYTHING THAT APPEARS NON-ENVIRONMENTALS

```html
<!DOCTYPE html>
<html lang="en">
<head>
<meta charset="utf-8">
<title>Kestrel Hub — Clean, Safe, Renewable</title>
<link href="https://fonts.googleapis.com/css2?family=Montserrat:wght@400;600;700;800&family=Open+Sans:wght@400;600&display=swap" rel="stylesheet">
<style>
:root{
  --green:#6fb52c;
  --green-light:#9fd65a;
  --forest:#1f3527;
  --forest-deep:#15251b;
  --forest-mid:#2a4333;
  --ink:#2f3a33;
  --muted:#85908a;
  --line:#e3e8e4;
  --tile:#dfe7dd;
  --white:#fff;
}
*{box-sizing:border-box;margin:0;padding:0}
html,body{width:1200px;height:4639px;overflow:hidden}
body{font-family:"Open Sans",Arial,sans-serif;color:var(--ink);background:var(--white);position:relative;font-size:13px}
h1,h2,h3,h4{font-family:"Montserrat",Arial,sans-serif}

/* top bar */
.topbar{position:absolute;top:0;left:0;width:1200px;height:87px;background:var(--forest-deep);color:#cfd8d1}
.topbar .hours{position:absolute;left:232px;top:8px;font-size:10px}
.topbar .follow{position:absolute;right:232px;top:8px;font-size:10px;display:flex;gap:8px;align-items:center}
.dot{width:8px;height:8px;background:#b9c6bc;display:inline-block}
.hcontact{position:absolute;top:38px;display:flex;align-items:center;gap:10px;color:#fff}
.hcontact .ico{width:30px;height:30px;border:2px solid var(--green);display:flex;align-items:center;justify-content:center}
.hcontact b{font-family:"Montserrat",sans-serif;font-size:18px;display:block;line-height:1}
.hcontact small{font-size:10px;color:#b9c6bc}

/* nav */
.nav{position:absolute;top:87px;left:0;width:1200px;height:52px;background:var(--green)}
.nav ul{list-style:none;position:absolute;left:232px;top:20px;display:flex;gap:40px;font-family:"Montserrat",sans-serif;font-weight:700;font-size:10px;color:#fff}
.nav .tools{position:absolute;right:232px;top:19px;display:flex;gap:22px}

/* hero */
.hero{position:absolute;top:139px;left:0;width:1200px;height:473px;background:linear-gradient(180deg,#3e4543 0%,#66695e 45%,#7f8a4c 62%,#6c7a2c 78%,#3f4f1d 100%)}
.frame{position:absolute;left:325px;top:124px;width:572px;height:232px}
.frame i{position:absolute;width:28px;height:28px;border-color:#fff;border-style:solid}
.frame .tl{left:0;top:0;border-width:2px 0 0 2px}.frame .tr{right:0;top:0;border-width:2px 2px 0 0}
.frame .bl{left:0;bottom:0;border-width:0 0 2px 2px}.frame .br{right:0;bottom:0;border-width:0 2px 2px 0}
.hero .txt{position:absolute;left:0;top:146px;width:1200px;text-align:center;color:#fff}
.hero .kick{font-size:11px;letter-spacing:1px;font-family:"Montserrat",sans-serif}
.hero h1{font-size:38px;font-weight:800;margin:6px 0 10px;letter-spacing:1px}
.hero p{font-size:11px;width:540px;margin:0 auto;line-height:1.6;color:#eee}
.btn{display:inline-block;background:var(--green);color:#fff;font-family:"Montserrat",sans-serif;font-weight:700;font-size:10px;padding:9px 20px}
.hero .btn{margin-top:24px}
.pager{position:absolute;right:22px;top:250px;display:flex;flex-direction:column;gap:8px}
.pager i{width:6px;height:6px;background:#fff;opacity:.6;display:block}

/* section title */
.stitle{position:absolute;left:0;width:1200px;text-align:center}
.stitle .box{display:inline-block;position:relative;padding:10px 28px 6px}
.stitle .box:before{content:"";position:absolute;left:0;top:0;width:24px;height:24px;border-left:3px solid var(--green);border-top:3px solid var(--green)}
.stitle h2{font-size:20px;font-weight:800;letter-spacing:1px}
.stitle small{font-size:9px;color:var(--muted);display:block;margin-top:2px}
.stitle p{width:560px;margin:14px auto 0;font-size:11px;color:var(--muted);line-height:1.6}

/* offer cards */
.card{position:absolute;top:810px;height:242px;background:#fff;box-shadow:0 2px 10px rgba(0,0,0,.08);text-align:center;padding-top:32px}
.card h3{font-size:11px;font-weight:700;margin:14px 0 10px}
.card p{font-size:9.5px;color:var(--muted);line-height:1.55;padding:0 26px}
.card .btn{margin-top:16px;padding:7px 16px;font-size:9px}
.card.photo{background:linear-gradient(180deg,#9aa8a4 0%,#c5cbc0 55%,#d3d6c5 100%)}
.card.photo .veil{position:absolute;inset:0;background:rgba(255,255,255,.55)}
.card.photo>*:not(.veil){position:relative}

/* projects */
.projects{position:absolute;top:1129px;left:0;width:1200px;height:511px;background:var(--forest);color:#fff}
.ptitle{position:absolute;left:232px;top:70px;padding:10px 0 0 14px}
.ptitle:before{content:"";position:absolute;left:0;top:0;width:24px;height:24px;border-left:3px solid var(--green);border-top:3px solid var(--green)}
.ptitle h2{font-size:20px;font-weight:800;line-height:1.3}
.projects p{position:absolute;left:232px;top:166px;width:350px;font-size:10px;color:#c2cec5;line-height:1.6}
.projects .btn{position:absolute;left:232px;top:236px;font-size:9px;padding:7px 14px}
.pimg{position:absolute;left:610px;top:77px;width:358px;height:272px;background:linear-gradient(180deg,#d9b27a 0%,#e3c9a0 40%,#6f7d86 62%,#3d5060 80%,#556b2f 100%)}
.thumbs{position:absolute;left:232px;top:294px;display:flex;gap:4px}
.thumbs div{width:92px;height:102px}
.projects .pn{position:absolute;left:232px;top:428px;font-size:9px;font-family:"Montserrat",sans-serif;color:#a9b8ad;display:flex;gap:30px}

/* why */
.why-title{position:absolute;left:232px;top:1700px;padding:10px 0 0 14px}
.why-title:before{content:"";position:absolute;left:0;top:0;width:24px;height:24px;border-left:3px solid var(--green);border-top:3px solid var(--green)}
.why-title h2{font-size:20px;font-weight:800}
.why-title small{font-size:9px;color:var(--muted);display:block;margin-top:2px}
.why-text{position:absolute;left:232px;top:1800px;width:200px;font-size:9.5px;color:var(--muted);line-height:1.6}
.feat{position:absolute;width:230px;display:flex;gap:12px}
.feat .ic{width:30px;height:30px;flex:none;border:1.5px solid var(--green);border-radius:50%;display:flex;align-items:center;justify-content:center}
.feat h4{font-size:9.5px;font-weight:700;margin-bottom:5px}
.feat p{font-size:9px;color:var(--muted);line-height:1.55}

/* stats */
.stats{position:absolute;top:1927px;left:0;width:1200px;height:155px;background:var(--forest)}
.stat{position:absolute;top:44px;width:150px;margin-left:-75px;text-align:center}
.stat b{font-family:"Montserrat",sans-serif;font-size:27px;color:var(--green-light);font-weight:700;display:block}
.stat span{font-size:8.5px;color:#c9d4cc;font-family:"Montserrat",sans-serif;letter-spacing:.5px}

/* services */
.services{position:absolute;top:2082px;left:0;width:1200px;height:516px;background:var(--forest-mid)}
.worker{position:absolute;left:0;top:0;width:572px;height:516px;background:linear-gradient(100deg,#6b86a8 0%,#8aa0b8 40%,#c9a34a 62%,#e2b52a 80%,#4e5b55 100%)}
.svc-title{position:absolute;left:600px;top:62px;padding:10px 0 0 14px;color:#fff}
.svc-title:before{content:"";position:absolute;left:0;top:0;width:24px;height:24px;border-left:3px solid var(--green);border-top:3px solid var(--green)}
.svc-title small{font-size:9px;color:#b9c6bc;display:block}
.svc-title h2{font-size:20px;font-weight:800}
.svc-text{position:absolute;left:612px;top:146px;width:350px;font-size:10px;color:#dde5df;line-height:1.6}
.tile{position:absolute;width:108px;height:105px;background:var(--tile);text-align:center;padding-top:24px}
.tile span{display:block;font-family:"Montserrat",sans-serif;font-size:8px;font-weight:700;margin-top:10px;line-height:1.4;color:#2f3a33}
.tile.on{background:var(--green)}.tile.on span{color:#fff}

/* blog */
.feature{position:absolute;left:232px;top:2836px;width:356px;height:235px;background:linear-gradient(180deg,#2e3634 0%,#4b5552 55%,#5f6a54 100%)}
.date{position:absolute;width:42px;height:42px;background:var(--green);text-align:center;font-family:"Montserrat",sans-serif;font-weight:700;color:#fff;padding-top:6px}
.date b{display:block;font-size:15px;line-height:1}.date small{font-size:8px}
.feature h3{position:absolute;left:20px;top:160px;font-size:12px;color:var(--green-light);font-weight:800;line-height:1.4}
.feature .meta{position:absolute;left:20px;bottom:14px;font-size:8px;color:#ccc}
.post{position:absolute;left:606px;width:362px;border-bottom:1px solid var(--line);padding-left:56px}
.post .date{left:0;top:0}
.post h4{font-size:9px;font-weight:700;padding-top:4px}
.post small{font-size:8px;color:var(--muted)}
.post p{font-size:9px;color:var(--muted);line-height:1.55;margin-top:6px}

/* testimonials */
.testi{position:absolute;top:3149px;left:0;width:1200px;height:399px;background:linear-gradient(180deg,#17251c 0%,#2c3d31 50%,#1c2a21 100%)}
.tcard{position:absolute;top:170px;width:238px;height:151px;background:#fff;text-align:center;padding:30px 22px 0}
.tcard p{font-size:9px;color:var(--muted);line-height:1.6}
.tcard h4{font-size:9px;font-weight:700;margin-top:14px}
.tcard small{font-size:8px;color:var(--muted)}
.avatar{position:absolute;left:50%;top:-22px;margin-left:-22px;width:44px;height:44px;border-radius:50%;border:3px solid var(--green);background:linear-gradient(180deg,#c9a98e,#8d6b55)}

/* contacts & booking */
.infobar{position:absolute;left:232px;top:3749px;width:736px;height:102px;background:#fff;box-shadow:0 2px 10px rgba(0,0,0,.07)}
.info{position:absolute;top:26px;display:flex;gap:12px}
.info h4{font-size:9px;font-weight:700;margin-bottom:4px}
.info p{font-size:9px;color:var(--muted);line-height:1.5}
.field{position:absolute;left:396px;width:408px;height:36px;border-bottom:1px solid var(--line);font-size:9px;color:#9aa39d;padding-top:14px}
.formbtn{position:absolute;left:535px;top:4116px}

/* partners */
.partners{position:absolute;top:4213px;left:0;width:1200px;height:127px;background:var(--green);display:flex;justify-content:space-around;align-items:center;padding:0 30px}
.partner{display:flex;align-items:center;gap:8px;font-family:"Montserrat",sans-serif;font-weight:700;font-size:16px;color:#fff}
.partner i{width:18px;height:18px;background:#fff;border-radius:50%;display:block}

/* footer */
.footer{position:absolute;top:4340px;left:0;width:1200px;height:299px;background:var(--forest-deep);color:#a9b5ad}
.fcol{position:absolute;top:72px;font-size:9px;line-height:1.7}
.fcol h4{font-size:10px;color:#fff;font-weight:700;margin-bottom:10px}
.socials{display:flex;gap:10px;margin-top:12px}
.socials i{width:10px;height:10px;background:#a9b5ad;display:block}
.subscribe{margin-top:10px;display:flex;border:1px solid #3a4d40;height:26px}
.subscribe span{flex:1;padding:4px 8px;color:#7d8c82;font-size:8.5px}
.subscribe b{background:var(--green);color:#fff;font-family:"Montserrat",sans-serif;font-size:8px;padding:5px 8px}
.fgal{width:164px;height:80px;background:linear-gradient(180deg,#7d8a96,#4f5e4a)}
.copy{position:absolute;left:0;bottom:12px;width:1200px;text-align:center;font-size:8.5px;color:#738078;border-top:1px solid #2b3a30;padding-top:10px}
</style>
</head>
<body>

<header class="topbar">
  <div class="hours">Opening Hours Mon – Sat 8.00 – 18.00</div>
  <div class="follow">Follow us: <i class="dot"></i><i class="dot"></i><i class="dot"></i><i class="dot"></i><i class="dot"></i></div>
  <div class="hcontact" style="left:640px">
    <div class="ico"><svg width="14" height="14" viewBox="0 0 24 24"><path d="M6.6 10.8a15 15 0 006.6 6.6l2.2-2.2a1 1 0 011-.25 11 11 0 003.6.6 1 1 0 011 1V20a1 1 0 01-1 1A17 17 0 013 4a1 1 0 011-1h3.5a1 1 0 011 1 11 11 0 00.6 3.6 1 1 0 01-.25 1z" fill="#6fb52c"/></svg></div>
    <div><b>0800 555 0142</b><small>hello@kestrelhub.com</small></div>
  </div>
  <div class="hcontact" style="left:842px">
    <div class="ico"><svg width="14" height="14" viewBox="0 0 24 24"><path d="M12 2a7 7 0 00-7 7c0 5 7 13 7 13s7-8 7-13a7 7 0 00-7-7zm0 9.5A2.5 2.5 0 1112 6.5a2.5 2.5 0 010 5z" fill="#6fb52c"/></svg></div>
    <div><b>27 Wattle Row</b><small>Dubbo, New South Wales</small></div>
  </div>
</header>

<nav class="nav">
  <ul><li>HOME</li><li>SERVICES</li><li>BOOKING</li><li>PRODUCTS</li><li>GALLERY</li><li>NEWS</li><li>CONTACTS</li></ul>
  <div class="tools">
    <svg width="14" height="14" viewBox="0 0 24 24"><circle cx="10" cy="10" r="6" fill="none" stroke="#fff" stroke-width="2.4"/><path d="M15 15l6 6" stroke="#fff" stroke-width="2.4"/></svg>
    <svg width="14" height="14" viewBox="0 0 24 24"><circle cx="12" cy="8" r="4" fill="none" stroke="#fff" stroke-width="2.2"/><path d="M4 21c1-5 15-5 16 0" fill="none" stroke="#fff" stroke-width="2.2"/></svg>
    <svg width="14" height="14" viewBox="0 0 24 24"><path d="M3 4h3l2 11h11l2-8H7" fill="none" stroke="#fff" stroke-width="2.2"/><circle cx="9" cy="20" r="1.6" fill="#fff"/><circle cx="18" cy="20" r="1.6" fill="#fff"/></svg>
  </div>
</nav>

<section class="hero" role="img" aria-label="Wind turbines standing in a green field under a stormy sky">
  <div class="frame"><i class="tl"></i><i class="tr"></i><i class="bl"></i><i class="br"></i></div>
  <div class="txt">
    <div class="kick">ENERGY AS CLEAN AS THE WIND</div>
    <h1>CLEAN, SAFE, RENEWABLE.</h1>
    <p>Join neighbours across regional Australia, buy solar and wind gear together, and cut power bills while cutting carbon from every home you power.</p>
    <span class="btn">Book Now</span>
  </div>
  <div class="pager"><i></i><i style="opacity:1"></i><i></i></div>
</section>

<div class="stitle" style="top:670px">
  <div class="box"><h2>WHAT WE OFFER</h2><small>BULK BUYING FOR GREEN HOMES</small></div>
  <p>We group conscious families so every order is bigger and every price is lower. Pick a system, join a buying round and let us handle the quotes, install and paperwork.</p>
</div>
<div class="card" style="left:232px;width:248px">
  <svg width="30" height="30" viewBox="0 0 30 30"><rect x="4" y="6" width="22" height="16" fill="none" stroke="#2f3a33" stroke-width="1.6"/><path d="M4 14h22M11 6v16M19 6v16M15 22v5M10 27h10" stroke="#2f3a33" stroke-width="1.6"/></svg>
  <h3>SOLAR SYSTEM</h3>
  <p>Rooftop panels sized for your home, bought in bulk rounds so every family in the group pays less.</p>
  <span class="btn">Read More</span>
</div>
<div class="card photo" style="left:483px;width:235px" role="img" aria-label="Wind turbines on a pale sky">
  <div class="veil"></div>
  <svg width="30" height="30" viewBox="0 0 30 30"><circle cx="15" cy="11" r="2" fill="#2f3a33"/><path d="M15 11L15 2M15 11l8 5M15 11l-8 5M15 13v15" stroke="#2f3a33" stroke-width="1.6"/></svg>
  <h3>WIND TURBINES</h3>
  <p>Small turbines for rural blocks, ordered together to lower freight and install costs for all.</p>
  <span class="btn">Read More</span>
</div>
<div class="card" style="left:721px;width:247px">
  <svg width="30" height="30" viewBox="0 0 30 30"><circle cx="15" cy="12" r="7" fill="none" stroke="#2f3a33" stroke-width="1.6"/><path d="M15 8v8M11 12h8M6 25h18M9 21v4M21 21v4" stroke="#2f3a33" stroke-width="1.6"/></svg>
  <h3>HEAT PUMPS</h3>
  <p>Efficient hot water and heating units that slash bills, with group prices across each round.</p>
  <span class="btn">Read More</span>
</div>

<section class="projects">
  <div class="ptitle"><h2>WE DO AWESOME WORKS,<br>SOME OF OUR PROJECT HERE.</h2></div>
  <p>From farm sheds near Orange to suburban roofs in Bendigo, our group rounds have powered hundreds of homes. Browse recent installs and see what joining a round could mean for your family.</p>
  <span class="btn">See All Projects</span>
  <div class="pimg" role="img" aria-label="Solar panel field and wind turbines at sunset with a city skyline"></div>
  <div class="thumbs">
    <div role="img" aria-label="Turbines at dusk" style="background:linear-gradient(180deg,#8ea0b2,#4b5a3c)"></div>
    <div role="img" aria-label="Sunlight over solar panels" style="background:linear-gradient(180deg,#d99a3c,#3a4a66)"></div>
    <div role="img" aria-label="Solar array close up" style="background:linear-gradient(180deg,#7fa4c9,#2e4a6e)"></div>
    <div role="img" aria-label="Rooftop installation" style="background:linear-gradient(180deg,#b9c2c8,#556066)"></div>
  </div>
  <div class="pn"><span>&larr; PREV</span><span>NEXT &rarr;</span></div>
</section>

<div class="why-title"><h2>WHY CHOOSE US</h2><small>WE MAKE GREEN AFFORDABLE</small></div>
<p class="why-text">More buyers mean better deals. We vet installers, compare products and keep you informed from the first quote to the final switch on.</p>
<div class="feat" style="left:458px;top:1725px"><div class="ic"><svg width="14" height="14" viewBox="0 0 24 24"><path d="M13 2L4 14h7l-1 8 9-12h-7z" fill="#6fb52c"/></svg></div><div><h4>NEWEST TECHNOLOGIES</h4><p>We only offer tested panels, inverters and batteries from trusted makers.</p></div></div>
<div class="feat" style="left:730px;top:1725px"><div class="ic"><svg width="14" height="14" viewBox="0 0 24 24"><circle cx="12" cy="12" r="5" fill="none" stroke="#6fb52c" stroke-width="2"/><path d="M12 1v4M12 19v4M1 12h4M19 12h4" stroke="#6fb52c" stroke-width="2"/></svg></div><div><h4>POWER AND ENERGY</h4><p>Systems sized to your use so you save from the very first bill.</p></div></div>
<div class="feat" style="left:458px;top:1812px"><div class="ic"><svg width="14" height="14" viewBox="0 0 24 24"><path d="M5 19C5 9 12 4 20 4c0 9-5 15-15 15zM5 19l8-8" fill="none" stroke="#6fb52c" stroke-width="2"/></svg></div><div><h4>TAKE CARE OF NATURE</h4><p>Every round cuts tonnes of carbon from regional homes each year.</p></div></div>
<div class="feat" style="left:730px;top:1812px"><div class="ic"><svg width="14" height="14" viewBox="0 0 24 24"><path d="M7 12l3 3 7-7" fill="none" stroke="#6fb52c" stroke-width="2.2"/></svg></div><div><h4>GREEN ENERGY</h4><p>Clean power that stays with your home for decades to come.</p></div></div>

<section class="stats">
  <div class="stat" style="left:309px"><b>2477</b><span>FINISHED PROJECTS</span></div>
  <div class="stat" style="left:458px"><b>832</b><span>HAPPY CLIENTS</span></div>
  <div class="stat" style="left:603px"><b>1858</b><span>WORKING HOURS</span></div>
  <div class="stat" style="left:749px"><b>10035</b><span>GROUP MEMBERS</span></div>
  <div class="stat" style="left:897px"><b>1858</b><span>TONNES CO2 SAVED</span></div>
</section>

<section class="services">
  <div class="worker" role="img" aria-label="Installer in work wear holding a yellow hard hat"></div>
  <div class="svc-title"><small>FROM QUOTE TO INSTALLATION</small><h2>SERVICES WE PROVIDE</h2></div>
  <p class="svc-text">Renewable energy, lighting systems, energy assessment, R.H.L.P scheme support and energy comparison, all handled by one team that puts your savings and the planet first.</p>
  <div class="tile" style="left:612px;top:213px"><svg width="22" height="22" viewBox="0 0 24 24"><path d="M9 18h6M10 21h4M12 3a6 6 0 00-3.5 10.9V16h7v-2.1A6 6 0 0012 3z" fill="none" stroke="#2f3a33" stroke-width="1.6"/></svg><span>RENEWABLE<br>ENERGY</span></div>
  <div class="tile" style="left:730px;top:213px"><svg width="22" height="22" viewBox="0 0 24 24"><path d="M12 3v3M5 6l2 2M19 6l-2 2M8 14a4 4 0 118 0v4H8z" fill="none" stroke="#2f3a33" stroke-width="1.6"/></svg><span>LIGHTING<br>SYSTEMS</span></div>
  <div class="tile" style="left:847px;top:213px"><svg width="22" height="22" viewBox="0 0 24 24"><rect x="5" y="3" width="14" height="18" fill="none" stroke="#2f3a33" stroke-width="1.6"/><path d="M8 8h8M8 12h8M8 16h5" stroke="#2f3a33" stroke-width="1.6"/></svg><span>ENERGY<br>ASSESSMENT</span></div>
  <div class="tile on" style="left:612px;top:334px"><svg width="22" height="22" viewBox="0 0 24 24"><path d="M7 12l3 3 7-7" fill="none" stroke="#fff" stroke-width="2"/><circle cx="12" cy="12" r="9" fill="none" stroke="#fff" stroke-width="1.6"/></svg><span>R.H.L.P<br>SCHEME</span></div>
  <div class="tile" style="left:730px;top:334px"><svg width="22" height="22" viewBox="0 0 24 24"><path d="M5 20V10M12 20V4M19 20v-7" stroke="#2f3a33" stroke-width="2"/></svg><span>ENERGY<br>COMPARISON</span></div>
  <div class="tile" style="left:847px;top:334px"><svg width="22" height="22" viewBox="0 0 24 24"><rect x="4" y="5" width="16" height="15" fill="none" stroke="#2f3a33" stroke-width="1.6"/><path d="M4 10h16M8 3v4M16 3v4" stroke="#2f3a33" stroke-width="1.6"/></svg><span>BOOK AN<br>APPOINTMENT</span></div>
</section>

<div class="stitle" style="top:2700px">
  <div class="box"><h2>NEW FROM BLOG</h2><small>IN THE NEWS</small></div>
  <p>Rebates, new tech and stories from our members. Stay up to date with the latest in clean energy across regional Australia.</p>
</div>
<article class="feature" role="img" aria-label="Wind turbine against a dark cloudy sky">
  <div class="date" style="left:0;top:0"><b>03</b><small>JUL</small></div>
  <h3>NEW REBATES OPEN FOR<br>REGIONAL SOLAR BUYERS</h3>
  <div class="meta">By Admin &nbsp;·&nbsp; 4 comments</div>
</article>
<div class="post" style="top:2836px;height:84px"><div class="date"><b>03</b><small>JUL</small></div><h4>WINTER ROUND: BATTERY PRICES DROP AGAIN</h4><small>By Admin</small><p>Our latest buying round locked in lower prices for home batteries across the state.</p></div>
<div class="post" style="top:2932px;height:50px"><div class="date"><b>08</b><small>JUL</small></div><h4>HOW GROUP BUYING CUTS INSTALL COSTS</h4><small>By Admin</small></div>
<div class="post" style="top:2994px;height:50px;border:0"><div class="date"><b>10</b><small>JUL</small></div><h4>FIVE WAYS TO LOWER YOUR WINTER POWER BILL</h4><small>By Admin</small></div>

<section class="testi" role="img" aria-label="Rows of solar panels at dusk">
  <div class="stitle" style="top:62px;color:#fff">
    <div class="box"><small style="color:#b9c6bc">WHAT MEMBERS SAY</small><h2>OUR TESTIMONIALS</h2></div>
  </div>
  <div class="tcard" style="left:232px"><div class="avatar" role="img" aria-label="Member portrait"></div><p>Our group round saved us almost a third on a full rooftop system. Simple, honest and fast.</p><h4>OWEN HARLOW</h4><small>Member, Tamworth</small></div>
  <div class="tcard" style="left:483px"><div class="avatar" role="img" aria-label="Member portrait"></div><p>They explained every rebate and compared quotes for us. Our bills have dropped right away.</p><h4>MAYA LINFIELD</h4><small>Member, Ballarat</small></div>
  <div class="tcard" style="left:730px"><div class="avatar" role="img" aria-label="Member portrait"></div><p>Great team, clear updates and a turbine that now powers most of our farm sheds.</p><h4>IVAN CASTELL</h4><small>Member, Mildura</small></div>
</section>

<div class="stitle" style="top:3610px">
  <div class="box"><small>CONTACT US</small><h2>OUR CONTACTS</h2></div>
  <p>Questions about a buying round, a quote or the R.H.L.P scheme? Reach our team by phone, email or visit our office.</p>
</div>
<div class="infobar">
  <div class="info" style="left:70px"><svg width="16" height="16" viewBox="0 0 24 24"><path d="M12 2a7 7 0 00-7 7c0 5 7 13 7 13s7-8 7-13a7 7 0 00-7-7zm0 9.5A2.5 2.5 0 1112 6.5a2.5 2.5 0 010 5z" fill="#6fb52c"/></svg><div><h4>HEAD OFFICE</h4><p>27 Wattle Row, Dubbo<br>New South Wales 2830</p></div></div>
  <div class="info" style="left:310px"><svg width="16" height="16" viewBox="0 0 24 24"><path d="M6.6 10.8a15 15 0 006.6 6.6l2.2-2.2a1 1 0 011-.25 11 11 0 003.6.6 1 1 0 011 1V20a1 1 0 01-1 1A17 17 0 013 4a1 1 0 011-1h3.5a1 1 0 011 1 11 11 0 00.6 3.6 1 1 0 01-.25 1z" fill="#6fb52c"/></svg><div><h4>CALL US</h4><p>0800 555 0142<br>Office: 02 5550 1870</p></div></div>
  <div class="info" style="left:530px"><svg width="16" height="16" viewBox="0 0 24 24"><rect x="3" y="5" width="18" height="14" fill="none" stroke="#6fb52c" stroke-width="2"/><path d="M3 6l9 7 9-7" fill="none" stroke="#6fb52c" stroke-width="2"/></svg><div><h4>EMAIL US</h4><p>hello@kestrelhub.com<br>rounds@kestrelhub.com</p></div></div>
</div>
<div class="stitle" style="top:3880px"><div class="box"><small>FREE HOME ENERGY VISIT</small><h2>BOOK AN APPOINTMENT</h2></div></div>
<div class="field" style="top:3955px">Your name</div>
<div class="field" style="top:3998px">Your email or phone</div>
<div class="field" style="top:4041px;height:60px">Preferred date and what you need help with</div>
<span class="btn formbtn">Book appointment</span>

<section class="partners">
  <div class="partner"><i></i>BRIGHTLEAF</div>
  <div class="partner"><i></i>SUNWELL</div>
  <div class="partner"><i></i>homegrid</div>
  <div class="partner"><i></i>GALEWORKS</div>
  <div class="partner"><i></i>TERRAMODE</div>
  <div class="partner"><i></i>Lumora</div>
</section>

<footer class="footer">
  <div class="fcol" style="left:232px;width:170px"><h4>KESTREL HUB</h4>We group green minded families to buy solar, wind and efficiency gear in bulk so everyone saves money and carbon.<div class="socials"><i></i><i></i><i></i><i></i></div></div>
  <div class="fcol" style="left:420px;width:150px"><h4>CONTACT US</h4>27 Wattle Row, Dubbo NSW<br>0800 555 0142<br>02 5550 1870<br>hello@kestrelhub.com<br>rounds@kestrelhub.com</div>
  <div class="fcol" style="left:600px;width:175px"><h4>NEWSLETTER</h4>Subscribe for new buying rounds, rebate news and saving tips.<div class="subscribe"><span>Your email</span><b>SUBSCRIBE</b></div></div>
  <div class="fcol" style="left:800px;width:170px"><h4>GALLERY</h4><div class="fgal" role="img" aria-label="Solar panels under a blue sky"></div></div>
  <div class="copy">© Kestrel Hub. All rights reserved.</div>
</footer>

</body>
</html>
```